Health IT software startup needs a product sheet to promote our software/company

-Need a one page product sheet that highlights our software and company for our customers.
-Our software is an EHR (electronic health record) software for hospitals.
-Attached is our logo (2 options-picture 4,5). Our caption with the logo should read "An EHR developed by physicians and healthcare professionals with decades of experience in behavioral health".
-Incorporate another smaller sub-heading (section) in the product sheet- titled "How Mendora Helps You"- with three associated words- 'Quality, Familiarity, Security'.
-Incorporate the main section titled "Our Software" with a description of the software with 3 components to use- see attached word document- Mendora Product Sheet.
-Attached is a optional photo you may consider if you like- we currently use it on our website with our logo and logo caption- see attached homepage-resized.jpg
-you can additional royalty free photos as needed
-Finally, the 'Contact Us' information:
404-612-8350
info@mendorasoftware.example
www.mendorasoftware.example

Target Market(s)

Behavioral Health Hospitals- specifically the product sheet will be left with the customers after we demo the software to them.

Font styles to use
Serif
Sans Serif

Colors
0555a3
3276b5
85acd3
0393ce
33a6d7
00a990
cedeed
ecf7fb
33b8a4

Requirements
Should not have
• Please do not saturate the product sheet with only colors- utilize white space

```html
<!DOCTYPE html>
<html lang="en">
<head>
<meta charset="utf-8">
<title>Mendora Product Sheet</title>
<link href="https://fonts.googleapis.com/css2?family=Quicksand:wght@400&family=Source+Sans+3:wght@300;400;600;700&family=Exo+2:ital,wght@1,700;1,800&display=swap" rel="stylesheet">
<style>
  :root{
    --navy:#0555a3;
    --blue-mid:#3276b5;
    --blue-soft:#85acd3;
    --cyan:#0393ce;
    --cyan-soft:#33a6d7;
    --teal:#00a990;
    --teal-soft:#33b8a4;
    --ice:#cedeed;
    --mist:#ecf7fb;
    --ink:#1f2d6b;
    --body:#2b3a5c;
    --band-dark:#0b3f86;
  }
  *{margin:0;padding:0;box-sizing:border-box}
  html,body{width:927px;height:1200px;overflow:hidden;background:#fff}
  .sheet{position:relative;width:927px;height:1200px;overflow:hidden;background:#fff;font-family:"Source Sans 3",sans-serif;color:var(--body)}

  .top-strip{position:absolute;left:0;top:0;width:927px;height:48px;background:linear-gradient(90deg,var(--band-dark),#1a5cab 70%,#2b6fba)}
  .brand-bar{position:absolute;left:0;top:48px;width:927px;height:124px;background:linear-gradient(180deg,#fff,#f3f7fb)}
  .brand{position:absolute;left:46px;top:68px;display:flex;align-items:center;gap:20px}
  .brand-mark{width:78px;height:78px;border-radius:50%;background:var(--navy)}
  .brand-name{font-family:"Quicksand",sans-serif;font-weight:400;font-size:72px;color:var(--ink);letter-spacing:1px;line-height:1}

  .hero-rule{position:absolute;left:0;top:172px;width:927px;height:6px;background:var(--blue-soft)}
  .hero{position:absolute;left:0;top:178px;width:927px;height:340px;
    background:linear-gradient(180deg,
      #0b478f 0%,
      #1458a6 38%,
      var(--blue-mid) 52%,
      var(--cyan-soft) 64%,
      var(--teal-soft) 74%,
      var(--ice) 86%,
      #ffffff 100%)}
  .tagline{position:absolute;right:26px;top:202px;text-align:right;color:#fff;font-size:21.5px;line-height:26px;font-weight:300}

  .section-title{position:absolute;left:174px;top:554px;font-family:"Exo 2",sans-serif;font-style:italic;font-weight:800;font-size:33px;color:var(--navy)}

  .feature{position:absolute;left:0;width:570px}
  .feature-badge{position:absolute;left:27px;width:136px;height:154px;display:flex;align-items:center;justify-content:center}
  .feature-badge svg{position:absolute;inset:0}
  .feature-label{position:relative;text-align:center;font-weight:700;font-size:13.5px;line-height:17px;color:var(--ink);text-transform:uppercase}
  .feature-text{position:absolute;left:185px;width:378px;font-size:13.4px;line-height:18px;text-align:justify;color:var(--body)}

  .helps{position:absolute;left:591px;top:542px;width:312px;height:386px;background:var(--navy)}
  .helps-title{position:absolute;left:0;width:312px;top:24px;text-align:center;font-family:"Exo 2",sans-serif;font-style:italic;font-weight:700;font-size:18px;color:#fff}
  .helps-item{position:absolute;left:30px;display:flex;align-items:center;gap:26px}
  .helps-icon{width:56px;height:56px;display:flex;align-items:center;justify-content:center}
  .helps-word{font-family:"Exo 2",sans-serif;font-style:italic;font-weight:700;font-size:33px;color:#fff}
  .helps-rule-a{position:absolute;left:591px;top:928px;width:312px;height:5px;background:var(--teal-soft)}
  .helps-rule-b{position:absolute;left:591px;top:933px;width:312px;height:4px;background:var(--cyan-soft)}

  .contact{position:absolute;left:591px;top:937px;width:312px;height:216px;background:var(--mist);text-align:center}
  .contact-title{margin-top:20px;font-family:"Exo 2",sans-serif;font-style:italic;font-weight:800;font-size:30px;color:var(--navy)}
  .contact-list{list-style:none;margin-top:18px;font-weight:700;font-size:16px;line-height:27.5px;color:var(--ink)}
</style>
</head>
<body>
<div class="sheet">
  <div class="top-strip"></div>
  <div class="brand-bar"></div>
  <div class="brand">
    <span class="brand-mark"></span>
    <span class="brand-name">Mendora</span>
  </div>

  <div class="hero-rule"></div>
  <div class="hero" role="img" aria-label="Header illustration of flowing blue, cyan and teal waves"></div>
  <p class="tagline">An EHR developed by physicians and healthcare professionals<br>with decades of experience in behavioral health</p>

  <h2 class="section-title">Our Software</h2>

  <section class="feature" style="top:620px">
    <div class="feature-badge" style="top:0">
      <svg viewBox="0 0 136 154" width="136" height="154" aria-hidden="true"><polygon points="68,0 136,38 136,116 68,154 0,116 0,38" fill="#ecf7fb"/></svg>
      <span class="feature-label">Organic<br>Documentation</span>
    </div>
    <p class="feature-text" style="top:5px">Mendora set out to provide behavioral health clinicians a familiar platform to engage in chart level documentation for their patient care. Our software is built using each company’s individualized workflow to provide efficient and valid information. By engaging in that recognized foundation, Mendora achieves the feel of an actual chart with the functionality of an electronic record.</p>
  </section>

  <section class="feature" style="top:800px">
    <div class="feature-badge" style="top:0">
      <svg viewBox="0 0 136 154" width="136" height="154" aria-hidden="true"><polygon points="68,0 136,38 136,116 68,154 0,116 0,38" fill="#ecf7fb"/></svg>
      <span class="feature-label">Patient<br>Engagement</span>
    </div>
    <p class="feature-text" style="top:-13px">Using our proprietary Mendora Modules, we seamlessly digitalize therapy for use in both individual and group therapy. An optional function of the software, Mendora Modules allow the clinician to individualize therapy in a hospital setting. Furthermore, we incorporate a Family Portal through the software so that therapy can involve the entire family during the client’s hospitalization. This allows the client’s support system to become an integral part of the client’s improvement in the hospital.</p>
  </section>

  <section class="feature" style="top:984px">
    <div class="feature-badge" style="top:0">
      <svg viewBox="0 0 136 154" width="136" height="154" aria-hidden="true"><polygon points="68,0 136,38 136,116 68,154 0,116 0,38" fill="#ecf7fb"/></svg>
      <span class="feature-label">Risk<br>Management<br>/<br>Quality<br>Improvement</span>
    </div>
    <p class="feature-text" style="top:-1px">To facilitate and navigate the ever-changing regulatory environment, Mendora built tailored risk management/quality improvement capabilities into the software. It is capable of tracking deficiencies in the documentation within the hospital, observing trends in real time to engage risk improvement measures, and providing data required for Quality Measures. Mendora feels this risk functionality will help identify potential errors and issues before they become systemic.</p>
  </section>

  <aside class="helps">
    <h3 class="helps-title">How Mendora Helps You?</h3>
    <div class="helps-item" style="top:82px">
      <span class="helps-icon"><svg width="52" height="50" viewBox="0 0 52 50" aria-hidden="true"><polygon points="26,1 32.5,18 51,18.5 36.5,30 41.5,48.5 26,38 10.5,48.5 15.5,30 1,18.5 19.5,18" fill="#fff"/></svg></span>
      <span class="helps-word">Quality</span>
    </div>
    <div class="helps-item" style="top:172px">
      <span class="helps-icon"><svg width="58" height="46" viewBox="0 0 58 46" aria-hidden="true" fill="#fff"><circle cx="11" cy="14" r="6"/><circle cx="47" cy="14" r="6"/><circle cx="29" cy="9" r="8"/><path d="M1 40 V30 a10 10 0 0 1 20 0 V40Z"/><path d="M37 40 V30 a10 10 0 0 1 20 0 V40Z"/><path d="M16 46 V31 a13 13 0 0 1 26 0 V46Z"/></svg></span>
      <span class="helps-word">Familiarity</span>
    </div>
    <div class="helps-item" style="top:262px">
      <span class="helps-icon"><svg width="34" height="50" viewBox="0 0 34 50" aria-hidden="true" fill="none" stroke="#fff" stroke-width="3"><path d="M8 22 V13 a9 9 0 0 1 18 0 V22"/><rect x="2" y="22" width="30" height="26" rx="3"/><circle cx="17" cy="33" r="3" fill="#fff" stroke="none"/><line x1="17" y1="34" x2="17" y2="41"/></svg></span>
      <span class="helps-word">Security</span>
    </div>
  </aside>
  <div class="helps-rule-a"></div>
  <div class="helps-rule-b"></div>

  <section class="contact">
    <h3 class="contact-title">Contact Us</h3>
    <ul class="contact-list">
      <li>404-612-8350</li>
      <li>info@mendorasoftware.example</li>
      <li>www.mendorasoftware.example</li>
    </ul>
  </section>
</div>
</body>
</html>
```